Design some Business Cards for eyelash / hair extensions

100% Guaranteed contest, check my history, perfect 5 star rating, I *always* select a winner and pay, even if we end up not using the winning design!!

Standard US size business cards, full color front and back.

You can see the information on the company and style here : [url removed, login to view]

Logo is attached.

Current card is attached - you can use the information on the card for your designs.

NOTES:

1) If we see something we like we will close the project early so get your work in quick!
2) Before selecting the winner, we sort by date to ensure you have not stolen your concept from someone else (no cheating!).
3) Final hand off design to be in adobe illustrator format - no exceptions!

Good luck!

```html
<!DOCTYPE html>
<html lang="en">
<head>
<meta charset="utf-8">
<title>Fringe &amp; Curl – Business Card</title>
<link rel="stylesheet" href="https://fonts.googleapis.com/css2?family=Cormorant+Garamond:wght@500&display=swap">
<style>
  :root {
    --bg-light: #e4edcb;
    --bg-mid: #c6d8a0;
    --bg-edge: #a9c27c;
    --leaf-light: rgba(226, 236, 196, 0.75);
    --leaf-deep: rgba(140, 170, 98, 0.55);
    --ink: #6a6a5e;
  }
  html, body {
    margin: 0;
    padding: 0;
    overflow: hidden;
  }
  .card {
    position: relative;
    width: 1200px;
    height: 685px;
    overflow: hidden;
    background: radial-gradient(ellipse 70% 80% at 48% 30%, var(--bg-light) 0%, var(--bg-mid) 60%, var(--bg-edge) 100%);
  }
  .leaf-spray {
    position: absolute;
    left: 560px;
    top: 0;
    width: 640px;
    height: 685px;
    background:
      radial-gradient(ellipse 22% 30% at 30% 22%, var(--leaf-light) 0%, transparent 75%),
      radial-gradient(ellipse 30% 42% at 55% 55%, var(--leaf-deep) 0%, transparent 75%),
      radial-gradient(ellipse 26% 34% at 88% 30%, var(--leaf-deep) 0%, transparent 75%),
      radial-gradient(ellipse 34% 30% at 40% 88%, var(--leaf-deep) 0%, transparent 75%);
  }
  .brand-name {
    margin: 0;
    font-family: "Cormorant Garamond", "Times New Roman", serif;
    font-weight: 500;
    font-size: 124px;
    line-height: 1;
    letter-spacing: 4px;
    color: var(--ink);
  }
  .brand-part {
    position: absolute;
    top: 268px;
    white-space: nowrap;
  }
  .brand-first { right: 680px; }
  .brand-join { left: 600px; }
  .brand-second { left: 733px; }
</style>
</head>
<body>
  <main class="card">
    <div class="leaf-spray" role="img" aria-label="Faint sweeping leaves and scroll curves"></div>
    <h1 class="brand-name">
      <span class="brand-part brand-first">Fringe</span>
      <span class="brand-part brand-join">&amp;</span>
      <span class="brand-part brand-second">Curl</span>
    </h1>
  </main>
</body>
</html>
```